business card with logo Marigold Nails & Spa 2815 SW Harlow Ave Portland OR 97099

Would like to have a business card with our logo.
like bottle of polish with our logo or letter M on it
want something that first glance would let you know that it is a nail salon.
like the hands with polish bottle dripping.
like black or White back ground

Marigold Nails & Spa
(The Velvet Retreat)
2815 SW Harlow Ave
Portland, OR 97099
Call or Text: 1-555-714-3928
www.MarigoldNailsnSpa.example
Open 7 days a week.
After 7:00 PM is by appointment only.
Closed only on Thanksgiving & Christmas.

Target Market(s)

20%Man and 80%Woman 13-70

Industry/Entity Type

Business

Contact Information for Business Card

Elegant with Logo-Business name- address-phone-open days. closed day.

Font styles to use
Decorative
Script

Colors
000000

Requirements
Must have
• Logo and place for Technician Name
• Marigold Nails & Spa
• (The Velvet Retreat)
• 2815 SW Harlow Ave
• Portland, OR 97099
• Call or Text: 1-555-714-3928
• Open 7 days a week
• Closed only on Thanksgiving & Christmas.
• We accepted all major credit cards but prefer cash. Thank you
Nice to have
• Nail polish bottle with our Logo or letter M
Should not have
• too colorful

```html
<!DOCTYPE html>
<html lang="en">
<head>
<meta charset="utf-8">
<title>Marigold Nails &amp; Spa – Business Card</title>
<link href="https://fonts.googleapis.com/css2?family=Source+Sans+3:ital,wght@1,400;1,600;1,700&display=swap" rel="stylesheet">
<style>
  :root {
    --backdrop: #7a7a7a;
    --red-light: #ee2a33;
    --red-deep: #c9000d;
    --white: #ffffff;
    --ink: #1a1a1a;
    --shape-a: #2b3a8c;
    --shape-b: #d32f2f;
    --shape-c: #2f7fc1;
    --shape-d: #e67e22;
  }
  * { margin: 0; padding: 0; box-sizing: border-box; }
  html, body { width: 1200px; height: 900px; overflow: hidden; }
  body {
    background: var(--backdrop);
    font-family: "Source Sans 3", "Myriad Pro", sans-serif;
    font-style: italic;
    position: relative;
  }
  .card {
    position: absolute;
    top: 170px;
    width: 347px;
    height: 560px;
    background: var(--white);
    overflow: hidden;
    text-align: center;
  }
  .card--front { left: 237px; }
  .card--back { left: 649px; }

  .band {
    position: absolute;
    left: 0;
    width: 100%;
    color: var(--white);
    background: radial-gradient(ellipse at 50% 45%, var(--red-light) 0%, #df0d18 55%, var(--red-deep) 100%);
  }
  .band--top { top: 0; height: 155px; }
  .band--bottom { top: 335px; height: 225px; }

  .tech-name { position: absolute; top: 34px; width: 100%; font-size: 25px; font-weight: 700; }
  .tech-role { position: absolute; top: 62px; width: 100%; font-size: 18px; }
  .phone { position: absolute; top: 112px; width: 100%; font-size: 15.5px; }

  .company { position: absolute; top: 36px; width: 100%; font-size: 25px; font-weight: 600; }
  .address { position: absolute; top: 88px; width: 100%; font-size: 15.5px; line-height: 21px; }
  .website { position: absolute; top: 172px; width: 100%; font-size: 15.5px; }

  .logo {
    position: absolute;
    left: 0;
    width: 100%;
    display: flex;
    align-items: center;
    justify-content: center;
    gap: 10px;
    color: var(--ink);
  }
  .logo--front { top: 215px; height: 60px; }
  .logo--back { top: 95px; height: 70px; }
  .logo-mark {
    width: 16px; height: 16px; border-radius: 50%;
    background: var(--ink);
  }
  .logo-name { font-size: 30px; font-weight: 600; }

  .hours {
    position: absolute;
    top: 263px;
    width: 100%;
    color: var(--ink);
    font-size: 15px;
    line-height: 22px;
  }
  .hours p + p { margin-top: 20px; }
  .hours .emphasis { font-weight: 700; }

  .payments {
    position: absolute;
    top: 481px;
    width: 100%;
    display: flex;
    justify-content: center;
    align-items: center;
    gap: 8px;
  }
  .pay-shape { height: 24px; border-radius: 2px; }
  .pay-shape--a { width: 38px; background: var(--shape-a); }
  .pay-shape--b { width: 50px; height: 30px; border-radius: 50%; background: var(--shape-b); }
  .pay-shape--c { width: 28px; height: 28px; background: var(--shape-c); }
  .pay-shape--d { width: 72px; height: 14px; background: var(--shape-d); }
</style>
</head>
<body>
  <section class="card card--front" aria-label="Card front">
    <div class="band band--top">
      <div class="tech-name">Lena Hartwell</div>
      <div class="tech-role">Director</div>
      <div class="phone">Call or Text : 1-555-714-3928</div>
    </div>

    <div class="logo logo--front">
      <span class="logo-mark"></span>
      <span class="logo-name">Marigold Nails n Spa</span>
    </div>

    <div class="band band--bottom">
      <div class="company">Marigold Nails &amp; Spa</div>
      <div class="address">
        (The Velvet Retreat)<br>
        2815 SW Harlow Ave<br>
        Portland, OR 97099
      </div>
      <div class="website">www.MarigoldNailsnSpa.example</div>
    </div>
  </section>

  <section class="card card--back" aria-label="Card back">
    <div class="logo logo--back">
      <span class="logo-mark"></span>
      <span class="logo-name">Marigold Nails n Spa</span>
    </div>

    <div class="hours">
      <p>Open 7 days a week.<br>After 7:00 PM is by appointment only.</p>
      <p class="emphasis">Closed only on Thanksgiving &amp; Christmas.</p>
      <p>We accepted all major credit cards but<br>prefer cash. Thank you</p>
    </div>

    <div class="payments" role="img" aria-label="Accepted payment cards">
      <span class="pay-shape pay-shape--a"></span>
      <span class="pay-shape pay-shape--b"></span>
      <span class="pay-shape pay-shape--c"></span>
      <span class="pay-shape pay-shape--d"></span>
    </div>
  </section>
</body>
</html>
```